I need a great, modern, professional website for my paint contracting company, Ashbrook Coating Contractors, LLC. I have many good pix that can be used from jobs completed that would be attractive. We do commercial, residential and industrial jobs. I’m fully insured and licensed, including holding a General Contractor’s License as a Subcontractor. I know nothing about coding websites. I’ll have my assistant get on tomorrow and learn how to drop files. I’m not sure what files to send. This will be difficult at best, it being able to talk this through. Oh well. What’s next?

Target Market(s)

General Contractors

Industry/Entity Type

Paint Contracting

Coding

Coded - Design and coding required

Font styles to use
Sans Serif

Colors
00AB8E
00BBA5
67D7C9
C6EFE9
E9F9F6

Requirements
Must have
• Pix of completed jobs, bio, maybe testimonials from happy customers? ….
Nice to have
• I’d like it to have a modern appeal, but still have some warmth.
Should not have
• ??

```html
<!DOCTYPE html>
<html lang="en">
<head>
<meta charset="utf-8">
<title>Ashbrook Coating Contractors, LLC</title>
<link href="https://fonts.googleapis.com/css2?family=Rubik:wght@400;500;600;700&family=Roboto:wght@400;500;700&display=swap" rel="stylesheet">
<style>
:root{
  --green:#00AB8E;
  --green-2:#0DB394;
  --teal:#00BBA5;
  --mint:#67D7C9;
  --ice:#C6EFE9;
  --frost:#E9F9F6;
  --ink:#111;
  --text:#333;
  --grey:#f6f6f6;
  --white:#fff;
}
*{box-sizing:border-box;margin:0;padding:0}
html,body{width:1200px;height:4354px;overflow:hidden}
body{position:relative;background:var(--white);font-family:"Roboto",Arial,sans-serif;color:var(--text)}
.abs{position:absolute}
.heading{font-family:"Rubik",Arial,sans-serif;font-weight:600;color:var(--ink);letter-spacing:.5px}
.btn{position:absolute;display:flex;align-items:center;justify-content:center;background:var(--green);color:var(--white);font-family:"Rubik",Arial,sans-serif;font-weight:600;border-radius:40px;text-transform:uppercase;letter-spacing:.5px}

/* header */
.site-header{left:0;top:0;width:1200px;height:123px;background:var(--frost)}
.brand{position:absolute;left:150px;top:20px;font-family:"Rubik",Arial,sans-serif;font-weight:600;color:var(--green);line-height:1}
.brand .line1{font-size:34px;display:block}
.brand .line2{font-size:24px;display:block;margin-top:4px}
.quote-btn{left:906px;top:22px;width:144px;height:36px;font-size:15px}
.main-nav{position:absolute;top:74px;left:583px;display:flex;gap:29px;font-size:14px;color:#444}
.main-nav .active{color:var(--green);font-weight:700}

/* hero */
.hero{left:0;top:123px;width:1200px;height:621px}
.hero-photo{position:absolute;inset:0;background:linear-gradient(100deg,#cdeef2 0%,#dff2f4 35%,#c9d6da 60%,#8e9aa0 80%,#6d7f8e 100%)}
.hero-edge{position:absolute;left:0;bottom:0;width:1200px;height:60px}
.hero-title{left:152px;top:142px;font-size:46px;line-height:58px;font-weight:700}
.learn-btn{left:154px;top:343px;width:176px;height:49px;font-size:19px}

/* about */
.about-title{left:150px;top:918px;font-size:45px;font-weight:700}
.about-text{left:150px;top:1007px;width:410px;font-size:13.4px;line-height:18.7px;color:#222}
.read-btn{left:150px;top:1230px;width:168px;height:51px;font-size:19px}
.about-art{left:600px;top:906px;width:462px;height:414px}

/* services */
.services{left:0;top:1453px;width:1200px;height:600px;background:linear-gradient(90deg,#fff 45%,var(--frost) 65%)}
.services-photo{position:absolute;left:0;top:0;width:544px;height:600px;background:linear-gradient(120deg,#d9d9d9 0%,#f2cf2f 30%,#f5d53a 45%,#4a6fa2 60%,#2e4f86 80%,#cfcfcf 100%)}
.services-title{left:629px;top:1541px;font-size:42px;font-weight:700}
.service{position:absolute;left:625px;width:440px;height:92px}
.service .icon{position:absolute;left:0;top:0;width:92px;height:92px;border-radius:50%;border:2px solid var(--green);background:var(--white);display:flex;align-items:center;justify-content:center}
.service h3{position:absolute;left:112px;top:10px;font-family:"Rubik",Arial,sans-serif;font-weight:500;font-size:19px;color:var(--ink)}
.service p{position:absolute;left:113px;top:40px;width:310px;font-size:11.4px;line-height:15px;color:#333}

/* jobs */
.jobs-band{left:0;top:2079px;width:1200px;height:625px;background:var(--grey)}
.jobs-title{left:0;top:2133px;width:1200px;text-align:center;font-size:44px;font-weight:700}
.job{position:absolute;left:242px;width:716px;height:163px;background:var(--white);border:1px solid #ddd;border-radius:10px;box-shadow:0 3px 8px rgba(0,0,0,.12)}
.job .thumb{position:absolute;left:12px;top:12px;width:169px;height:138px;border-radius:6px}
.job h3{position:absolute;top:24px;font-family:"Rubik",Arial,sans-serif;font-weight:500;font-size:19.5px;color:var(--ink)}
.job p{position:absolute;top:60px;width:450px;font-size:12.6px;line-height:18.5px;color:#222}
.job .type{position:absolute;top:115px;display:flex;align-items:center;gap:10px;font-size:13.5px;color:#222}
.job .more{position:absolute;top:114px;width:101px;height:30px;border-radius:20px;font-family:"Rubik",Arial,sans-serif;font-weight:600;font-size:11px;display:flex;align-items:center;justify-content:center;letter-spacing:.5px}
.more.fill{background:var(--green);color:var(--white)}
.more.line{border:2px solid var(--green);color:var(--green);background:var(--white)}
.view-btn{left:515px;top:2827px;width:168px;height:51px;font-size:19px}

/* process */
.process-band{left:0;top:2966px;width:1200px;height:296px;background:var(--frost)}
.process-title{left:0;top:3028px;width:1200px;text-align:center;font-size:44px;font-weight:700}
.step{position:absolute;top:3151px;width:230px;text-align:center}
.step .disc{width:204px;height:204px;margin:0 auto;border-radius:50%;background:var(--green);display:flex;align-items:center;justify-content:center}
.step h3{margin-top:30px;font-family:"Rubik",Arial,sans-serif;font-weight:500;font-size:22px;color:var(--ink)}
.step p{margin-top:10px;font-size:11.6px;line-height:14px;color:#222}

/* contact */
.contact-band{left:0;top:3772px;width:1200px;height:582px;background:var(--green-2)}
.footer-photo{left:0;top:4010px;width:700px;height:290px;background:radial-gradient(ellipse at 35% 45%,rgba(255,255,255,.14),rgba(255,255,255,0) 65%)}
.contact-card{left:154px;top:3569px;width:890px;height:433px;background:#e6f3f1;border-radius:110px 0 110px 0;border:5px solid var(--white);border-top:none;border-left-color:transparent}
.contact-title{left:0;top:3618px;width:1200px;text-align:center;font-size:43px;font-weight:700}
.field{position:absolute;background:var(--white);border:1.5px solid var(--green);font-size:12px;color:#555;padding:11px 14px}
.submit-btn{left:536px;top:3892px;width:128px;height:49px;font-size:18px}

/* footer */
.foot-brand{left:150px;top:4096px;font-family:"Rubik",Arial,sans-serif;font-weight:600;color:var(--white);line-height:1}
.foot-brand .line1{font-size:34px;display:block}
.foot-brand .line2{font-size:24px;display:block;margin-top:4px}
.socials{left:150px;top:4189px;display:flex;gap:15px}
.socials span{width:29px;height:29px;border-radius:50%;background:var(--white);display:block}
.foot-col{position:absolute;top:4104px;color:var(--white)}
.foot-col h4{font-family:"Rubik",Arial,sans-serif;font-weight:500;font-size:21px;margin-bottom:14px}
.foot-col li{list-style:none;font-size:13.5px;line-height:23px}
.contact-line{display:flex;align-items:flex-start;gap:10px;font-size:13.5px;line-height:16px;margin-bottom:17px}
.contact-line .ic{width:26px;height:26px;flex:none;border-radius:50%;background:var(--white);display:flex;align-items:center;justify-content:center}
.copyright{left:0;top:4301px;width:1200px;border-top:1px solid rgba(255,255,255,.35);padding-top:16px;text-align:center;color:var(--white);font-size:13.5px}
</style>
</head>
<body>

<header class="abs site-header">
  <div class="brand"><span class="line1">Ashbrook Coating</span><span class="line2">Contractors, LLC</span></div>
  <div class="btn quote-btn">Get a quote</div>
  <nav class="main-nav"><span class="active">Home</span><span>About</span><span>Our Services</span><span>Projects</span><span>Careers</span><span>Contact</span></nav>
</header>

<section class="abs hero">
  <div class="hero-photo" role="img" aria-label="Painter rolling light blue paint onto a wall"></div>
  <svg class="hero-edge" viewBox="0 0 1200 60" preserveAspectRatio="none" aria-hidden="true"><path d="M0 28 Q60 18 120 30 T260 26 T420 34 T600 24 T780 32 T960 26 T1200 30 V60 H0Z" fill="#fff"/></svg>
  <h1 class="abs heading hero-title">Welcome To<br>Ashbrook Coating<br>Contractors,LLC</h1>
  <div class="btn learn-btn">Learn more</div>
</section>

<h2 class="abs heading about-title">ABOUT US</h2>
<p class="abs about-text">Lorem ipsum dolor sit amet, consectetur adipiscing elit, sed do eiusmod tempor incididunt ut labore et dolore magna aliqua. Ut enim ad minim veniam, quis nostrud exercitation ullamco laboris nisi ut aliquip ex ea commodo consequat. Duis aute irure dolor in reprehenderit in voluptate velit esse cillum dolore eu fugiat nulla accusantium doloremque laudantium, totam rem aperiam, eaque ipsa quae ab illo inventore veritatis et quasi architecto beatae vitae dicta sunt explicabo. Nemo enim ipsam voluptatem quia voluptas sit aspernatur aut odit aut fugit, sed quia consequuntur magni dolores eos qui ratione voluptatem sequi nesciunt.</p>
<div class="btn read-btn">Read more</div>
<svg class="abs about-art" viewBox="0 0 462 414" role="img" aria-label="Smiling painter in blue overalls with a roller, and paint being poured into a tray">
  <defs>
    <linearGradient id="aboutBack" x1="0" y1="0" x2="1" y2="1"><stop offset="0" stop-color="#e8e8e6"/><stop offset="1" stop-color="#cfcfcc"/></linearGradient>
    <linearGradient id="aboutWorker" x1="0" y1="0" x2="0" y2="1"><stop offset="0" stop-color="#d9d4cc"/><stop offset=".45" stop-color="#3d6aa8"/><stop offset="1" stop-color="#1f4b82"/></linearGradient>
    <radialGradient id="aboutPour" cx=".5" cy=".5" r=".6"><stop offset="0" stop-color="#9cc34a"/><stop offset=".6" stop-color="#3a5fa8"/><stop offset="1" stop-color="#2a3f80"/></radialGradient>
  </defs>
  <rect x="230" y="205" width="232" height="209" fill="var(--green)"/>
  <polygon points="0 403 250 0 448 0 448 403" fill="url(#aboutBack)"/>
  <rect x="250" y="0" width="198" height="403" fill="url(#aboutWorker)"/>
  <circle cx="130" cy="170" r="133" fill="#fff"/>
  <circle cx="130" cy="170" r="125" fill="url(#aboutPour)"/>
</svg>

<section class="abs services">
  <div class="services-photo" role="img" aria-label="Painter in a hard hat rolling yellow paint onto a wall"></div>
</section>
<h2 class="abs heading services-title">WHAT WE DO?</h2>
<div class="service" style="top:1638px">
  <div class="icon"><svg width="50" height="50" viewBox="0 0 50 50" aria-hidden="true"><path d="M6 24 L25 8 L44 24" fill="none" stroke="#222" stroke-width="3"/><rect x="12" y="23" width="26" height="20" fill="var(--mint)" stroke="#222" stroke-width="2.5"/><rect x="21" y="31" width="8" height="12" fill="#f2b705"/></svg></div>
  <h3>Resedential Painting</h3>
  <p>Lorem ipsum dolor sit amet, consectetur adipiscing elit, sed do eiusmod tempor incididunt ut labore et dolore aliqua.</p>
</div>
<div class="service" style="top:1763px">
  <div class="icon"><svg width="50" height="50" viewBox="0 0 50 50" aria-hidden="true"><rect x="10" y="10" width="16" height="32" fill="#555" stroke="#222" stroke-width="2"/><rect x="26" y="20" width="14" height="22" fill="var(--mint)" stroke="#222" stroke-width="2"/><rect x="30" y="26" width="14" height="6" fill="#e65b2c"/></svg></div>
  <h3>Commercial Painting</h3>
  <p>Lorem ipsum dolor sit amet, consectetur adipiscing elit, sed do eiusmod tempor incididunt ut labore et dolore aliqua.</p>
</div>
<div class="service" style="top:1888px">
  <div class="icon"><svg width="50" height="50" viewBox="0 0 50 50" aria-hidden="true"><rect x="10" y="8" width="28" height="10" rx="2" fill="#f2b705" stroke="#222" stroke-width="2"/><path d="M38 13 H42 V24 H24 V30" fill="none" stroke="#222" stroke-width="2.5"/><rect x="21" y="30" width="6" height="14" rx="2" fill="var(--green)"/></svg></div>
  <h3>Industrial Painting</h3>
  <p>Lorem ipsum dolor sit amet, consectetur adipiscing elit, sed do eiusmod tempor incididunt ut labore et dolore aliqua.</p>
</div>

<div class="abs jobs-band"></div>
<h2 class="abs heading jobs-title">RECENT JOBS</h2>

<article class="job" style="top:2236px">
  <div class="thumb" role="img" aria-label="Painter on a ladder painting a house exterior" style="background:linear-gradient(180deg,#5f8fc4 0%,#9cb9d8 35%,#e4d8c0 60%,#9a8f82 100%)"></div>
  <h3 style="left:201px">Lorem Ipsum dolor sit amet consecuter</h3>
  <p style="left:203px">Lorem ipsum dolor sit amet, consectetur adipiscing elit, sed do eiusmod tempor incididunt ut labore et dolore magna aliqua.</p>
  <div class="type" style="left:203px"><svg width="26" height="26" viewBox="0 0 26 26" aria-hidden="true"><circle cx="13" cy="13" r="11" fill="none" stroke="var(--green)" stroke-width="2" stroke-dasharray="52 8"/><circle cx="13" cy="10" r="3.5" fill="var(--green)"/><path d="M7 19 Q13 12 19 19" fill="var(--green)"/></svg>Full Time</div>
  <div class="more fill" style="left:540px">READ MORE</div>
</article>

<article class="job" style="top:2434px">
  <div class="thumb" role="img" aria-label="Painter on scaffolding painting a building facade" style="background:linear-gradient(180deg,#ece6d6 0%,#c9c2b0 45%,#5d6b4e 70%,#3b3b3b 100%)"></div>
  <h3 style="right:58px;text-align:right">Lorem Ipsum dolor sit amet consecuter</h3>
  <p style="right:58px;text-align:right">Lorem ipsum dolor sit amet, consectetur adipiscing elit, sed do eiusmod tempor incididunt ut labore et dolore magna aliqua.</p>
  <div class="more line" style="left:220px">READ MORE</div>
  <div class="type" style="left:561px"><svg width="26" height="26" viewBox="0 0 26 26" aria-hidden="true"><circle cx="13" cy="13" r="11" fill="none" stroke="var(--green)" stroke-width="2" stroke-dasharray="52 8"/><circle cx="13" cy="10" r="3.5" fill="var(--green)"/><path d="M7 19 Q13 12 19 19" fill="var(--green)"/></svg>Full Time</div>
</article>

<article class="job" style="top:2628px">
  <div class="thumb" role="img" aria-label="Painter on a step ladder rolling an interior wall" style="background:linear-gradient(180deg,#d4d4d4 0%,#c6c6c6 50%,#6a7fb6 65%,#d0d0d0 100%)"></div>
  <h3 style="left:201px">Lorem Ipsum dolor sit amet consecuter</h3>
  <p style="left:203px">Lorem ipsum dolor sit amet, consectetur adipiscing elit, sed do eiusmod tempor incididunt ut labore et dolore magna aliqua.</p>
  <div class="type" style="left:203px"><svg width="26" height="26" viewBox="0 0 26 26" aria-hidden="true"><circle cx="13" cy="13" r="11" fill="none" stroke="var(--green)" stroke-width="2" stroke-dasharray="52 8"/><circle cx="13" cy="10" r="3.5" fill="var(--green)"/><path d="M7 19 Q13 12 19 19" fill="var(--green)"/></svg>Full Time</div>
  <div class="more fill" style="left:540px">READ MORE</div>
</article>

<div class="btn view-btn">View more</div>

<div class="abs process-band"></div>
<h2 class="abs heading process-title">SEE HOW WE WORK</h2>
<div class="step" style="left:137px">
  <div class="disc"><svg width="140" height="110" viewBox="0 0 140 110" aria-hidden="true" fill="#fff"><circle cx="70" cy="26" r="18"/><circle cx="32" cy="36" r="13"/><circle cx="108" cy="36" r="13"/><rect x="46" y="50" width="48" height="52" rx="12"/><rect x="12" y="56" width="32" height="46" rx="10"/><rect x="96" y="56" width="32" height="46" rx="10"/></svg></div>
  <h3>Step 1</h3>
  <p>Lorem ipsum dolor sit dolor amet,<br>consectetur dolorena aliqua.</p>
</div>
<div class="step" style="left:370px">
  <div class="disc"><svg width="130" height="120" viewBox="0 0 130 120" aria-hidden="true"><path d="M12 46 Q12 10 55 10 Q98 10 98 46 Q98 80 55 80 Q44 80 36 77 L14 90 L22 70 Q12 60 12 46Z" fill="#fff"/><path d="M104 44 Q122 52 122 70 Q122 84 112 92 L118 110 L98 98 Q92 100 84 100 Q64 100 56 88" fill="none" stroke="#fff" stroke-width="8"/><circle cx="36" cy="46" r="6" fill="var(--green)"/><circle cx="55" cy="46" r="6" fill="var(--green)"/><circle cx="74" cy="46" r="6" fill="var(--green)"/></svg></div>
  <h3>Step 2</h3>
  <p>Lorem ipsum dolor sit dolor amet,<br>consectetur dolorena aliqua.</p>
</div>
<div class="step" style="left:600px">
  <div class="disc"><svg width="120" height="150" viewBox="0 0 120 150" aria-hidden="true" fill="#fff"><circle cx="48" cy="40" r="12"/><path d="M36 56 H62 L84 30 L92 36 L68 70 V140 H56 V104 H48 V140 H36Z"/><rect x="78" y="8" width="34" height="14" rx="3"/><rect x="92" y="22" width="4" height="14"/><path d="M14 100 H38 V128 Q26 134 14 128Z"/></svg></div>
  <h3>Step 3</h3>
  <p>Lorem ipsum dolor sit dolor amet,<br>consectetur dolorena aliqua.</p>
</div>
<div class="step" style="left:831px">
  <div class="disc"><svg width="164" height="32" viewBox="0 0 164 32" aria-hidden="true" fill="#fff"><g id="star"><path d="M16 1 L20 11 L31 12 L22.5 19 L25.5 30 L16 24 L6.5 30 L9.5 19 L1 12 L12 11Z"/></g><use href="#star" x="33"/><use href="#star" x="66"/><use href="#star" x="99"/><use href="#star" x="132"/></svg></div>
  <h3>Step 4</h3>
  <p>Lorem ipsum dolor sit dolor amet,<br>consectetur dolorena aliqua.</p>
</div>

<div class="abs contact-band"></div>
<div class="abs footer-photo" role="img" aria-label="Faint background photo of a painter at work"></div>
<div class="abs contact-card"></div>
<h2 class="abs heading contact-title">CONTACT US</h2>
<div class="field" style="left:245px;top:3701px;width:237px;height:37px">Name</div>
<div class="field" style="left:488px;top:3701px;width:237px;height:37px">Email Address</div>
<div class="field" style="left:732px;top:3701px;width:218px;height:37px">Phone number</div>
<div class="field" style="left:245px;top:3752px;width:710px;height:165px;padding-top:14px">Message</div>
<div class="btn submit-btn">Submit</div>

<div class="abs foot-brand"><span class="line1">Ashbrook Coating</span><span class="line2">Contractors, LLC</span></div>
<div class="abs socials" aria-label="Social media links"><span></span><span></span><span></span></div>

<div class="foot-col" style="left:499px">
  <h4>Get In Touch</h4>
  <div class="contact-line"><span class="ic"><svg width="14" height="16" viewBox="0 0 14 16" aria-hidden="true"><path d="M7 1 A5.5 5.5 0 0 1 12.5 6.5 C12.5 10 7 15 7 15 C7 15 1.5 10 1.5 6.5 A5.5 5.5 0 0 1 7 1Z" fill="var(--green)"/><circle cx="7" cy="6.5" r="2" fill="#fff"/></svg></span><span>123 ipsum dolor sit amet,<br>consectetur st 123/4</span></div>
  <div class="contact-line"><span class="ic"><svg width="14" height="14" viewBox="0 0 14 14" aria-hidden="true"><path d="M3 1 L5.5 1 L6.5 4.5 L5 5.8 Q6.5 8.5 8.2 9 L9.5 7.5 L13 8.5 L13 11 Q12 13 9.5 12.5 Q2 10 1.5 3.5 Q1.5 1.5 3 1Z" fill="var(--green)"/></svg></span><span style="padding-top:5px">888 888 8888</span></div>
  <div class="contact-line"><span class="ic"><svg width="14" height="10" viewBox="0 0 14 10" aria-hidden="true"><rect x="0.5" y="0.5" width="13" height="9" rx="1" fill="var(--green)"/><path d="M1 1 L7 6 L13 1" fill="none" stroke="#fff" stroke-width="1.2"/></svg></span><span style="padding-top:5px">info@ashbrookcoating.com</span></div>
</div>
<div class="foot-col" style="left:781px">
  <h4>Explore</h4>
  <ul><li>Home</li><li>About</li><li>Our Services</li><li>Projects</li><li>Careers</li><li>Contact</li></ul>
</div>
<div class="foot-col" style="left:950px">
  <h4>Policies</h4>
  <ul><li>Privacy Policy</li><li>Terms &amp; Conditions</li><li>Legal Cookies</li></ul>
</div>
<div class="abs copyright">Copyright © 2023 Ashbrook Coating Contractors, LLC</div>

</body>
</html>
```